Web design for a Crane & Heavy Equipment Inspection, Repair and Maintenance Company in Texas

We need a web design for a new company based in Houston, Texas called "Kelder Crane & Equipment". We inspect, repair and maintain diesel driven heavy equipment, generators, fire water pumps and cranes. We would like to see designs that use the colors orange, white, yellow and brown, and/or orange, white, navy, yellow and grey.

```html
<!DOCTYPE html>
<html lang="en">
<head>
<meta charset="utf-8">
<title>Kelder Crane &amp; Equipment</title>
<link href="https://fonts.googleapis.com/css2?family=Ubuntu:wght@400;500;700&family=Quicksand:wght@400;500&family=Nunito:wght@400;600&display=swap" rel="stylesheet">
<style>
:root{
  --orange:#f05a28;
  --orange-dark:#d8461a;
  --navy:#1f4e7d;
  --navy-panel:rgba(31,78,125,.92);
  --text:#5a5a5a;
  --heading:#444;
  --band:#f2f2f2;
  --contact-band:#ebedee;
  --footer:#2b2b2b;
  --white:#fff;
}
*{box-sizing:border-box;margin:0;padding:0}
html,body{width:703px;height:1200px;overflow:hidden;background:var(--white)}
body{position:relative;font-family:'Nunito',sans-serif;color:var(--text)}
.abs{position:absolute}

.brand{left:50px;top:40px;font-family:'Ubuntu',sans-serif;font-weight:700;font-size:30px;line-height:32px;color:var(--navy);display:flex;align-items:center;gap:10px}
.brand-mark{width:16px;height:16px;background:var(--orange);border-radius:50%}
.brand small{display:block;font-size:17px;line-height:22px}
.header-phone{right:32px;top:54px;font-family:'Ubuntu',sans-serif;font-size:16px;color:var(--navy);display:flex;align-items:center;gap:8px}
.search{left:499px;top:90px;width:152px;height:21px;border:1px solid #ccc;font-size:9px;color:#888;padding:4px 8px;display:flex;justify-content:space-between;align-items:center}

.nav{left:50px;top:135px;width:602px;height:34px;display:flex;background:var(--orange)}
.nav a{flex:auto;display:flex;align-items:center;justify-content:center;font-family:'Ubuntu',sans-serif;font-weight:500;font-size:10.5px;color:var(--white);text-decoration:none;border-right:1px solid rgba(255,255,255,.3)}
.nav a:last-child{border-right:none}
.nav a.current{background:var(--orange-dark)}

.hero{left:51px;top:169px;width:601px;height:264px;overflow:hidden;background:linear-gradient(180deg,#a7c7e4 0%,#cfe0ee 60%,#c9c3a8 100%)}
.hero-photo{position:absolute;inset:0}
.hero-panel{position:absolute;inset:0;background:var(--navy-panel);clip-path:polygon(472px 0,601px 0,601px 264px,328px 264px)}
.hero-title{position:absolute;left:405px;top:113px;font-family:'Ubuntu',sans-serif;font-weight:500;font-size:22px;color:var(--white)}
.hero-text{position:absolute;left:405px;top:143px;width:180px;font-size:10.5px;line-height:16px;color:var(--white)}
.dots{position:absolute;left:536px;top:226px;display:flex;gap:4px}
.dots span{width:9px;height:9px;border-radius:50%;background:rgba(255,255,255,.55)}
.dots span:first-child{background:var(--white)}

.welcome{left:0;top:466px;width:703px;text-align:center;font-family:'Quicksand',sans-serif;font-size:20px;color:var(--heading)}
.welcome .accent{color:var(--orange)}
.welcome .navy{color:var(--navy)}
.intro{left:56px;top:502px;width:591px;text-align:center;font-size:8.5px;line-height:14px}
.btn{left:313px;top:560px;width:75px;height:24px;background:var(--navy);color:var(--white);font-family:'Ubuntu',sans-serif;font-size:11px;display:flex;align-items:center;justify-content:center;border-radius:2px}

.services{left:0;top:609px;width:703px;height:246px;background:var(--band)}
.service{position:absolute;top:36px;width:181px;text-align:center}
.service-img{height:101px;box-shadow:0 4px 4px -2px rgba(0,0,0,.25)}
.service h3{margin-top:19px;font-family:'Ubuntu',sans-serif;font-weight:500;font-size:12px;color:var(--navy)}
.service p{margin-top:8px;font-size:8.5px;line-height:15px}

.testi-title{left:0;top:886px;width:703px;text-align:center;font-family:'Quicksand',sans-serif;font-size:20px;color:var(--heading)}
.avatar-ring{left:55px;top:906px}
.avatar{position:absolute;left:62px;top:910px;width:104px;height:104px;border-radius:50%;background:radial-gradient(circle at 50% 40%,#d6b59a 0%,#b88d6e 45%,#d9d9d9 75%)}
.quote-badge{position:absolute;left:137px;top:987px;width:40px;height:40px;border-radius:50%;background:var(--white);display:flex;align-items:center;justify-content:center;font-family:Georgia,serif;font-size:30px;font-weight:700;color:#bbb;line-height:1}
.quote{left:204px;top:935px;width:475px;font-size:8.5px;line-height:15px;padding-left:14px}
.quote .q{font-family:Georgia,serif;font-size:16px;color:#aaa;font-weight:700}
.quote .open{position:absolute;left:0;top:-2px}
.author{left:218px;top:992px;font-size:10px;color:#333}
.author small{font-size:8.5px}

.contact-band{left:0;top:1063px;width:703px;height:66px;background:var(--contact-band)}
.contact-item{position:absolute;top:0;height:66px;display:flex;align-items:center;gap:12px;font-family:Arial,sans-serif;font-size:10px;color:#555}
.contact-item small{display:block;font-size:8.5px;color:#777;margin-top:4px}
.divider{position:absolute;top:21px;width:1px;height:26px;background:#ccc}

.footer{left:0;top:1129px;width:703px;height:71px;background:var(--footer);color:var(--white);font-family:Arial,sans-serif;font-size:8.5px}
.footer-links{position:absolute;left:51px;top:24px}
.copyright{position:absolute;left:51px;top:45px}
.social{position:absolute;left:517px;top:24px;display:flex;gap:8px}
.social span{width:21px;height:21px;display:block}
</style>
</head>
<body>

<div class="abs brand"><span class="brand-mark"></span><div>KELDER CRANE<small>&amp; EQUIPMENT</small></div></div>
<div class="abs header-phone">+1 713 555 0148
  <svg width="12" height="14" viewBox="0 0 24 24"><path fill="#1f4e7d" d="M6.6 10.8a15 15 0 0 0 6.6 6.6l2.2-2.2a1 1 0 0 1 1-.25 11.4 11.4 0 0 0 3.6.57 1 1 0 0 1 1 1V20a1 1 0 0 1-1 1A17 17 0 0 1 3 4a1 1 0 0 1 1-1h3.5a1 1 0 0 1 1 1c0 1.25.2 2.45.57 3.6a1 1 0 0 1-.25 1z"/></svg>
</div>
<div class="abs search"><span>Search..</span>
  <svg width="9" height="9" viewBox="0 0 10 10"><circle cx="4" cy="4" r="3" fill="none" stroke="#999" stroke-width="1.3"/><path d="M6.3 6.3 9 9" stroke="#999" stroke-width="1.3"/></svg>
</div>

<nav class="abs nav">
  <a class="current" href="#">HOME</a><a href="#">ABOUT</a><a href="#">CRANES</a><a href="#">SERVICES OFFERED</a><a href="#">BLOG</a><a href="#">TESTIMONIALS</a><a href="#">CONTACT</a>
</nav>

<section class="abs hero">
  <div class="hero-photo" role="img" aria-label="Yellow mobile crane truck parked on a site under a blue sky"></div>
  <div class="hero-panel"></div>
  <h2 class="hero-title">AENEAN COMDO</h2>
  <p class="hero-text">Eodem modo typi, qui nunc nobis vide ntur parum clari, fiant sollemnes infut.</p>
  <div class="dots"><span></span><span></span><span></span><span></span></div>
</section>

<h1 class="abs welcome">Welcome to <span class="accent">KELDER</span> <span class="navy">CRANE &amp; EQUIPMENTS</span></h1>
<p class="abs intro">Typi non habent claritatem insitam; est usus legentis in iis qui facit eorum claritatem. Investigationes demonstraverunt lectores legere me lquod ii unt saepius. Clarit as est etiam processus dynamicus, qui sequitur mutationem consuetudium lectorum. Mirum est notare quam litteothica, quam nunc putamus aramnimut litterarum formas humanitatis per seacula quarta decima et quinta decima. Eodem modo typi, qui nunc nobis videntur parum clari, fiant sollemnes in futurum.</p>
<div class="abs btn">Read More</div>

<section class="abs services">
  <div class="service" style="left:50px">
    <div class="service-img" role="img" aria-label="Tower cranes silhouetted against a dusk sky" style="background:linear-gradient(180deg,#1d2c44 0%,#4c6482 60%,#c9a26e 100%)"></div>
    <h3>INSPECT</h3>
    <p>Nullam sed nisi arcu condinm varius. Etiam malesuada velit bibeumdonec sit amet orci augue tristique eros amet risus</p>
  </div>
  <div class="service" style="left:258px">
    <div class="service-img" role="img" aria-label="Welder repairing a red crane boom" style="background:linear-gradient(135deg,#d63a4a 0%,#e7606c 50%,#a9c9e6 100%)"></div>
    <h3>REPAIR</h3>
    <p>Nullam sed nisi arcu condinm varius. Etiam malesuada velit bibeumdonec sit amet orci augue tristique eros amet risus</p>
  </div>
  <div class="service" style="left:471px">
    <div class="service-img" role="img" aria-label="Crane equipment under maintenance in a workshop" style="background:linear-gradient(180deg,#6a6d72 0%,#b7bcc2 55%,#8a4a3c 100%)"></div>
    <h3>MAINTAIN</h3>
    <p>Nullam sed nisi arcu condinm varius. Etiam malesuada velit bibeumdonec sit amet orci augue tristique eros amet risus</p>
  </div>
</section>

<h2 class="abs testi-title">Testimonials</h2>
<svg class="abs avatar-ring" width="120" height="136" viewBox="0 0 120 136">
  <path d="M60 134 L48 116 A58 58 0 1 1 72 116 Z" fill="#fff" stroke="#eee" stroke-width="2"/>
</svg>
<div class="avatar" role="img" aria-label="Portrait of the client giving the testimonial"></div>
<div class="quote-badge">&ldquo;</div>
<p class="abs quote"><span class="q open">&ldquo;</span>Duis rutrum eros orci, at tristique nulla dictum id. Donec porta justo non justo ultrices mattis. Nullam nec tortor eleifend, molestie quam ac, pretium quam. Nulla at pulvinar purus. Sed tristique elementum sapien sit amet porttitor. Duis eget consectetur et tortor ac libero gravida porttitor at et justo.&nbsp; libero gravida porttitor at et justo. <span class="q">&rdquo;</span></p>
<p class="abs author">- Marcus, <small>Austria</small></p>

<section class="abs contact-band">
  <div class="contact-item" style="left:68px">
    <svg width="16" height="22" viewBox="0 0 16 22"><path d="M8 0a8 8 0 0 0-8 8c0 6 8 14 8 14s8-8 8-14a8 8 0 0 0-8-8z" fill="#444"/><circle cx="8" cy="8" r="3" fill="#ebedee"/></svg>
    <div>Duis autem vel eum iriureHendrerit.<small>Typi non habent claritatem insitam</small></div>
  </div>
  <div class="divider" style="left:279px"></div>
  <div class="contact-item" style="left:315px">
    <svg width="16" height="18" viewBox="0 0 24 24"><path fill="#444" d="M6.6 10.8a15 15 0 0 0 6.6 6.6l2.2-2.2a1 1 0 0 1 1-.25 11.4 11.4 0 0 0 3.6.57 1 1 0 0 1 1 1V20a1 1 0 0 1-1 1A17 17 0 0 1 3 4a1 1 0 0 1 1-1h3.5a1 1 0 0 1 1 1c0 1.25.2 2.45.57 3.6a1 1 0 0 1-.25 1z"/></svg>
    <div>123 - 456 - 789</div>
  </div>
  <div class="divider" style="left:437px"></div>
  <div class="contact-item" style="left:473px">
    <svg width="26" height="17" viewBox="0 0 26 17"><rect width="26" height="17" fill="#444"/><path d="M1 1l12 9 12-9" fill="none" stroke="#ebedee" stroke-width="1.5"/></svg>
    <div>info@kelderservice.com</div>
  </div>
</section>

<footer class="abs footer">
  <div class="footer-links">Terms and Conditions | Privacy Promise | FAQ's | Contact Us</div>
  <div class="copyright">Copyright &copy; 2013. All Rights Reserved.</div>
  <div class="social" aria-label="Social links">
    <span style="background:#3b5998"></span><span style="background:#2a9fd8"></span><span style="background:#f27a1a"></span><span style="background:#d82624"></span>
  </div>
</footer>

</body>
</html>
```